Verlotti Magician

I want the business card for my business to give to people who watch that later I will be employed to show magic here is my website http://www.verlottimagicien.net/I want the interesting design , i am very opened for formal and informal, I watch a lot of design so don't stick to the common shape and form but i hope it can also be produced the thing to write on will be the same as in picture that i will upload , i also will upload the logo for you that so can be easy to useDenis CostilleMagicianMAGICIAN VERLOTTI 17 rue des Tilleuls - 25000 BESANÇON contact@verlottimagicien.net tel. 0384 519 467 tel. 0672 904 153

```html
<!DOCTYPE html>
<html lang="fr">
<head>
<meta charset="utf-8">
<title>Verlotti Magicien – Business Card</title>
<link rel="stylesheet" href="https://fonts.googleapis.com/css2?family=Lato:wght@300;400&display=swap">
<style>
  :root {
    --backdrop: #e9e6e1;
    --card: #ffffff;
    --ink: #111111;
    --ink-soft: #2a2a2a;
    --portrait: #1a1a1a;
    --shadow: rgba(0,0,0,0.18);
  }
  * { box-sizing: border-box; margin: 0; padding: 0; }
  html, body { width: 1200px; height: 942px; overflow: hidden; }
  body {
    background: var(--backdrop);
    font-family: "Lato", sans-serif;
    color: var(--ink);
    display: flex;
    align-items: center;
    justify-content: center;
    gap: 60px;
  }
  .card {
    position: relative;
    width: 520px;
    height: 300px;
    background: var(--card);
    box-shadow: 0 10px 28px var(--shadow);
  }

  /* Brand block */
  .brand { position: absolute; display: flex; align-items: center; gap: 14px; }
  .brand-portrait { background: var(--portrait); border-radius: 50%; }
  .brand-name {
    font-weight: 300;
    letter-spacing: 0.14em;
    color: var(--ink);
    line-height: 1;
  }

  /* Back side */
  .card-back .brand { top: 34px; left: 40px; }
  .card-back .brand-portrait { width: 86px; height: 86px; }
  .card-back .brand-name { font-size: 26px; }

  .holder { position: absolute; top: 150px; right: 40px; text-align: right; }
  .holder-name { font-size: 28px; font-weight: 400; letter-spacing: 0.02em; text-transform: uppercase; }
  .holder-role { font-size: 13px; font-weight: 300; letter-spacing: 0.12em; text-transform: uppercase; margin-top: 2px; }

  .contact { position: absolute; left: 40px; bottom: 26px; list-style: none; }
  .contact li {
    display: flex; align-items: center; justify-content: flex-end; gap: 8px;
    font-size: 13px; font-weight: 300; letter-spacing: 0.03em;
    text-transform: uppercase; color: var(--ink-soft); line-height: 1.55;
  }
  .contact svg { width: 13px; height: 13px; flex: none; }

  /* Front side */
  .card-front .brand { flex-direction: column; gap: 12px; top: 50%; left: 50%; transform: translate(-50%, -50%); }
  .card-front .brand-portrait { width: 120px; height: 120px; }
  .card-front .brand-name { font-size: 32px; }
</style>
</head>
<body>

  <section class="card card-back" aria-label="Card back">
    <div class="brand">
      <div class="brand-portrait" role="img" aria-label="Portrait illustration of the magician holding a card"></div>
      <span class="brand-name">VERLOTTI</span>
    </div>

    <div class="holder">
      <p class="holder-name">Hugo Marsenac</p>
      <p class="holder-role">Magician</p>
    </div>

    <ul class="contact">
      <li>17 rue des Tilleuls - 25000 Besançon
        <svg viewBox="0 0 24 24" aria-hidden="true"><path fill="currentColor" d="M12 2a7 7 0 0 0-7 7c0 5 7 13 7 13s7-8 7-13a7 7 0 0 0-7-7zm0 9.5A2.5 2.5 0 1 1 12 6.5a2.5 2.5 0 0 1 0 5z"/></svg></li>
      <li>contact@verlottimagicien.net
        <svg viewBox="0 0 24 24" aria-hidden="true"><path fill="currentColor" d="M2 5h20v14H2z"/><path fill="none" stroke="#fff" stroke-width="2" d="M3 6l9 7 9-7"/></svg></li>
      <li>www.verlottimagicien.net
        <svg viewBox="0 0 24 24" aria-hidden="true"><g fill="none" stroke="currentColor" stroke-width="2"><circle cx="12" cy="12" r="10"/><path d="M2 12h20M12 2c3 3 3 17 0 20M12 2c-3 3-3 17 0 20"/></g></svg></li>
      <li>0384 519 467/0672 904 153
        <svg viewBox="0 0 24 24" aria-hidden="true"><path fill="currentColor" d="M6.6 10.8a15 15 0 0 0 6.6 6.6l2.2-2.2a1 1 0 0 1 1-.25 11.4 11.4 0 0 0 3.6.57 1 1 0 0 1 1 1V20a1 1 0 0 1-1 1A17 17 0 0 1 3 4a1 1 0 0 1 1-1h3.5a1 1 0 0 1 1 1c0 1.25.2 2.45.57 3.6a1 1 0 0 1-.25 1z"/></svg></li>
    </ul>
  </section>

  <section class="card card-front" aria-label="Card front">
    <div class="brand">
      <div class="brand-portrait" role="img" aria-label="Portrait illustration of the magician holding a card"></div>
      <span class="brand-name">VERLOTTI</span>
    </div>
  </section>

</body>
</html>
```